Letterhead & Business Card for our Professional Practice (Financial Services)

We are looking for someone to design a letterhead and business card for our business, which is a professional practice called Harbor Lumen Capital Limited. The website is at www.harborrlumencapital.example.co.uk.

The letterhead needs to have: (a) our logo (b) address (c) telephone number (d) email address and (e) our company number.

We would like the stationary to be consistent with the website.

I have attached the logo in EPS and PNG format.

Target Market(s)

Professional services, large commercial enterprises, financial services

Industry/Entity Type

Financial Service

Font styles to use
Serif

Colors
3176b5
f04a50

Requirements
Must have
• Be consistent with our website located at www.harborlumencapital.example.co.uk
• Be in the following formats:
• 1. Word template for the letterhead
• 2. PDF for the letterhead with setup and bleeds required at www.presskite.example.co.uk
• 3. PDF for the business card with setup and bleeds required at www.presskite.example.co.uk
Nice to have
• Something with a really interesting design that says "these guys are professional but dynamic and interesting"
Should not have
• Boring

```html
<!DOCTYPE html>
<html lang="en">
<head>
<meta charset="utf-8">
<title>Harbor Lumen Capital – Stationery</title>
<link rel="stylesheet" href="https://fonts.googleapis.com/css2?family=Belleza&family=Jost:wght@400;500&display=swap">
<style>
  :root {
    --navy: #003a6b;
    --red: #cc1530;
    --paper: #ffffff;
    --backdrop: #f6f6f6;
  }
  * { box-sizing: border-box; margin: 0; padding: 0; }
  html, body {
    width: 1200px; height: 1001px; overflow: hidden;
    background: var(--backdrop);
  }
  .stationery { position: relative; width: 1200px; height: 1001px; }
  .sheet {
    position: absolute; background: var(--paper); overflow: hidden;
  }
  .letterhead { left: 158px; top: 135px; width: 490px; height: 693px; }
  .card-front { left: 708px; top: 226px; width: 357px; height: 214px; }
  .card-back  { left: 708px; top: 520px; width: 357px; height: 213px; }

  .brand {
    position: absolute; left: 0; right: 0;
    display: flex; flex-direction: column; align-items: center;
  }
  .brand-mark { background: var(--red); }
  .brand-name {
    font-family: "Belleza", "Optima", sans-serif;
    color: var(--navy); white-space: nowrap; line-height: 1;
  }
  .letterhead .brand { top: 22px; }
  .letterhead .brand-mark { width: 52px; height: 52px; margin-bottom: 10px; }
  .letterhead .brand-name { font-size: 22px; }
  .card-front .brand { top: 44px; }
  .card-front .brand-mark { width: 52px; height: 52px; margin-bottom: 10px; }
  .card-front .brand-name { font-size: 22px; }
  .card-back .brand { top: 21px; }
  .card-back .brand-mark { width: 25px; height: 25px; margin-bottom: 5px; }
  .card-back .brand-name { font-size: 11px; }

  .holder-name {
    position: absolute; left: 0; right: 0; top: 90px;
    text-align: center; font-family: "Jost", sans-serif;
    font-size: 31px; color: var(--navy); line-height: 1;
  }
  .contact {
    position: absolute; left: 0; right: 0; text-align: center;
    font-family: "Jost", sans-serif; color: var(--navy);
  }
  .letterhead .contact { top: 623px; font-size: 11px; line-height: 11.6px; }
  .card-back .contact { top: 163px; font-size: 8px; line-height: 8.4px; }

  .bands { position: absolute; left: 0; bottom: 0; width: 100%; display: block; }
  .band-left { fill: var(--navy); }
  .band-right { fill: var(--red); }
</style>
</head>
<body>
<main class="stationery">

  <section class="sheet letterhead" aria-label="Letterhead">
    <div class="brand">
      <span class="brand-mark"></span>
      <span class="brand-name">Harbor Lumen Capital</span>
    </div>
    <address class="contact">
      14-16 Quayside Row , Ashford , Kentshire , QR2 5LP<br>
      01632 960418<br>
      contact@harborlumencapital.example.co.uk<br>
      Registration number : 09142736
    </address>
    <svg class="bands" width="490" height="68" viewBox="0 0 490 68" aria-hidden="true">
      <polygon class="band-left" points="0,0 245,68 0,68"/>
      <polygon class="band-right" points="490,0 490,68 245,68"/>
    </svg>
  </section>

  <section class="sheet card-front" aria-label="Business card front">
    <div class="brand">
      <span class="brand-mark"></span>
      <span class="brand-name">Harbor Lumen Capital</span>
    </div>
    <svg class="bands" width="357" height="50" viewBox="0 0 357 50" aria-hidden="true">
      <polygon class="band-left" points="0,0 178,50 0,50"/>
      <polygon class="band-right" points="357,0 357,50 178,50"/>
    </svg>
  </section>

  <section class="sheet card-back" aria-label="Business card back">
    <div class="brand">
      <span class="brand-mark"></span>
      <span class="brand-name">Harbor Lumen Capital</span>
    </div>
    <h1 class="holder-name">Your Name</h1>
    <address class="contact">
      14-16 Quayside Row , Ashford , Kentshire , QR2 5LP<br>
      01632 960418<br>
      contact@harborlumencapital.example.co.uk<br>
      Registration number : 09142736
    </address>
    <svg class="bands" width="357" height="49" viewBox="0 0 357 49" aria-hidden="true">
      <polygon class="band-left" points="0,0 178,49 0,49"/>
      <polygon class="band-right" points="357,0 357,49 178,49"/>
    </svg>
  </section>

</main>
</body>
</html>
```